Renamed Motel Needs Appealing Flyer

We need a flyer design for a motel that has been closed for 3 years and has just reopened under new management. It has been renamed 'Tallowind Motel' and is located in the Grampians in Vic. We would like our design to showcase the beauty and magnificence of the Grampians National Park (Gariwerd being the Aboriginal name for the Park). The motel is an older style building, so we don't want photos of the building to be the focus of the flyer until we have had time to renovate etc.
http://www.filedrovex.com/file/9tq2pm
I will add a high res image of the motel name/logo on Monday
http://www.filedrovex.com/file/9tq2pm to see an additional photo. I will add a high res image of motel name/logo on Monday
all ages, backpackers, budget consious travellers, seniors, groups
- Flyer must be DL size (front and back only) with logo at the top so that it is visible when displayed in a tiered display rack. I am not sure if the logo I have provided is adequate resolution wise. Can you let me know if it is not? The 'points' under the name are not part of the logo and should be removed.
Suggested wording for front of flyer - Surrounded by rugged mountain ranges and native plants and animals, Tallowind Motel is the perfect base to explore the natural beauty of the Grampians.
Back of flyer - features: affordable accommodation, 25 spacious ground floor rooms,
single/twin/triple/quadruple rooms; queen beds; ensuite bathrooms/some rooms with baths; toaster/ tea and coffee making facilities; iron/ironing board in rooms; digital TV; free WiFi; microwaves for guest use; free BBQ facilities; breakfast available; conference facility for up to 25 persons
Address - 14 Brackley Rd, Mossvale 3274
Phone: (03) 5471 2098
Email: tallowindmotel@quokmail.com
www.tallowindmotel.com.au
Updated after first set of submissions/comments - 10.55 PM AEST.
The following text only should be for the front of the brochure - Surrounded by rugged mountain ranges and native plants and animals, Tallowind Motel is the perfect base to explore the natural beauty of the Grampians.
Logically then, listings from the original brief such as 'Surrounded by mountains' would not be relevant for the back.
The dot points listed above in the first brief, should then be the focus for the information and detail on the back of the brochure.
Another update is;
- correct display is R/Trak
- I would like the flyer to have a flowing feel, print over top of scenery images, different fonts. Perhaps back of flyer could be printed over a washed image of Grampians

```html
<!DOCTYPE html>
<html lang="en">
<head>
<meta charset="utf-8">
<title>Tallowind Motel – DL Flyer</title>
<link rel="stylesheet" href="https://fonts.googleapis.com/css2?family=Tinos:wght@400;700&display=swap">
<style>
  :root {
    --stage: #2c2b2a;
    --cream: #fbf8dc;
    --forest: #1f5a2c;
    --forest-deep: #174a23;
    --leaf: #2c6b33;
    --sky: #9cb8cf;
    --ridge: #3f6a3a;
    --rock: #a8843e;
    --wash: #e8eef0;
    --white: #ffffff;
  }
  * { box-sizing: border-box; margin: 0; padding: 0; }
  html, body { width: 1200px; height: 1184px; overflow: hidden; }
  body {
    background: var(--stage);
    font-family: "Tinos", "Times New Roman", serif;
    position: relative;
  }
  .flyer {
    position: absolute;
    top: 32px;
    width: 523px;
    height: 1114px;
    overflow: hidden;
  }
  .flyer--front { left: 43px; background: var(--cream); }
  .flyer--back { left: 632px; background: var(--wash); }

  .brand-panel {
    position: absolute;
    background: var(--forest);
    border: 4px solid var(--leaf);
    outline: 2px solid var(--cream);
    display: flex;
    align-items: center;
    justify-content: center;
    color: var(--white);
    font-weight: 700;
    z-index: 2;
  }
  .flyer--front .brand-panel { left: 34px; top: 32px; width: 454px; height: 148px; font-size: 52px; }
  .flyer--back .brand-panel { left: 145px; top: 805px; width: 233px; height: 77px; font-size: 28px; }

  .photo { position: absolute; left: 0; width: 100%; }
  .photo--valley {
    top: 105px; height: 483px;
    background: linear-gradient(180deg, var(--sky) 0%, #b9c9c9 20%, #6f8a62 38%, var(--ridge) 60%, #2f5a2c 100%);
  }
  .photo--rock {
    top: 836px; height: 278px;
    background: linear-gradient(180deg, var(--cream) 0%, #e2cf95 25%, var(--rock) 55%, #6d5a2a 80%, #4d5a2a 100%);
  }
  .photo--building {
    top: 0; height: 350px;
    background: linear-gradient(180deg, #dfe8ee 0%, #b7a56a 30%, #5b6b3a 60%, #55544c 100%);
  }
  .photo--wash {
    top: 350px; height: 493px;
    background: linear-gradient(180deg, #f2f5f6 0%, #dfe7ea 45%, #cfdad6 75%, #c3d0c5 100%);
  }

  .intro {
    position: absolute;
    left: 40px; right: 40px; top: 398px;
    color: var(--white);
    font-size: 19px;
    line-height: 1.36;
    text-align: center;
    text-shadow: 0 1px 3px rgba(0,0,0,.6);
  }

  .features {
    position: absolute;
    left: 20px; right: 20px;
    text-align: center;
    color: var(--forest);
  }
  .features h2 { font-weight: 400; }
  .features ul { list-style: none; }
  .features li::before { content: "• "; }

  .features--key { top: 608px; }
  .features--key h2 { font-size: 31px; margin-bottom: 6px; }
  .features--key li { font-size: 18px; line-height: 1.5; }
  .features--key li.wrap { line-height: 1.2; margin: 3px 0; }

  .features--facilities { top: 378px; }
  .features--facilities h2 { font-size: 28px; margin-bottom: 2px; letter-spacing: .3px; }
  .features--facilities li { font-size: 20px; line-height: 31.7px; }

  .contact {
    position: absolute;
    left: 0; top: 843px; width: 100%; height: 271px;
    background: var(--forest-deep);
    color: var(--white);
    text-align: center;
    padding-top: 52px;
    font-size: 22px;
    line-height: 34px;
  }
  .contact h3 { font-size: 26px; font-weight: 700; line-height: 36px; }
</style>
</head>
<body>
  <section class="flyer flyer--front">
    <div class="brand-panel">Tallowind Motel</div>
    <div class="photo photo--valley" role="img" aria-label="Aerial view of forested Grampians mountain ranges and valley"></div>
    <p class="intro">Surrounded by rugged mountain ranges and native plants and animals, Tallowind Motel is the perfect base to explore the natural beauty of the Grampians.</p>
    <div class="photo photo--rock" role="img" aria-label="Sunlit sandstone cliffs of a Grampians peak above bushland"></div>
    <div class="features features--key">
      <h2>KEY FEATURES</h2>
      <ul>
        <li>Surrounded by the mountains</li>
        <li class="wrap">Easy 5 minute walk from the centre<br>of Mossvale</li>
        <li>100 metres from R-Trak bus stop</li>
        <li>Affordable accommodation</li>
        <li>25 spacious ground floor rooms</li>
      </ul>
    </div>
  </section>

  <section class="flyer flyer--back">
    <div class="photo photo--building" role="img" aria-label="Motel entrance sign and ground floor units with parked cars among gum trees"></div>
    <div class="photo photo--wash" role="img" aria-label="Faded washed view of Grampians mountain ridges"></div>
    <div class="features features--facilities">
      <h2>TALLOWIND MOTEL FACILITIES</h2>
      <ul>
        <li>Single/twin/triple/quadruple rooms</li>
        <li>Queen beds</li>
        <li>Ensuite bathrooms/some rooms with baths</li>
        <li>Toaster/ tea and coffee making facilities</li>
        <li>Iron/ironing board in rooms</li>
        <li>Digital TV</li>
        <li>Free WiFi</li>
        <li>Microwaves for guest use</li>
        <li>Free BBQ facilities</li>
        <li>Breakfast available</li>
        <li>Conference facility for up to 25 persons</li>
      </ul>
    </div>
    <div class="contact">
      <h3>Contact Us At</h3>
      <p>Tallowind Hotel</p>
      <p>14 Brackley Rd, Mossvale 3274</p>
      <p>Phone: (03) 5471 2098</p>
      <p>Email: tallowindmotel@quokmail.com</p>
      <p>www.tallowindmotel.com.au</p>
    </div>
    <div class="brand-panel">Tallowind Motel</div>
  </section>
</body>
</html>
```